Come crowdsource a Web Design for a brazilian crowdsource Startup!

> NAME OF OUR STARTUP:
Vantremo

> DESCRIPTION OF OUR STARTUP:
We are a crowdsourcing startup in Brazil providing consultancy and technology to support other companies to crowdsource their projects.
We also operate doing big crowdsource campaings related to polemic subjects in Brazil.

> WHAT ARE OUR TARGET AUDIENCE?
Our target audience are young people around 20-35 years old.
Generation Y (Millennial Generation)

> WHAT IS OUR INDUSTRY?
Internet, web

> WHAT DO WE NEED?
We need a Web Design for our first site.

We need 5 pages:
- Home
- What is Crowdsourcing?
- Solutions
- About Us
- Blog
- A box for the "Contact" tab (this is not a page)

Please, find attached a Layout Sketch of what I've imagined.

Lets talk about the sketch:
Well, first of all, it's a SKETCH, so you don't have to send proposals exactly as the sketch. The sketch is just to show how I've imagined the ditribution of the content boxes. For example, the menu bar doesnt need to be a rectangle exactly like the sketch, but, I would like to have the menu on the right side of the logo. Also, you will see that the boxes are all squeezed, of course I dont want them soo squeezed! Again, its juust a SKETCH!

About the images on the sketch:
IMG1 - Some nice and simple image related to collectivity or related to crowdsourcing or maybe use our O logo.

IMG2 - Some simple and creative image related to Consultancy. It doesnt need to be so obvious.

IMG3 - Some simple and creative image related to Web 2.0 Software Technology. It doesnt need to be so obvious.

IMG4 - Some simple and creative image related to a full package of Consultancy + Technology. It doesnt need to be so obvious.

IMG5 - Some nice and simple image related to collectivity or related to crowdsourcing.

IMG6 - Some nice and simple image related to Ideation. Maybe a light bulb? I dont know, be creative!

IMG7 - Some nice and simple image related to Crowdlabor. I dont know, be creative!

IMG8 - Some nice and simple image related to CrowdFeedback. Maybe a megaphone? A loudspeaker? I dont know, be creative!

IMG9 - Some nice and simple image related to us! Maybe our O logo ? I dont know, be creative!

THE CONTACT SIDE BAR - we need a nice and simple contact side bar. By the way, on the sketch this bar is shown only at the homepage, but when the site becomes real this bar will stay along all the pages.

THE CONTACT BOX - we need a nice and simple contact box.

ABOUT THE COLORS TO USE: we would like some color to our background and titles. We like colors similars to our logo: really light blue ? light green/blue ? light grey ? light orange ? I dont know, you guys knows more about that then me =)

PLIMBOOK SHARE/LIKE BUTTON: We would like a plimbook share/like button somewhere on the site!

ABOUT THE ATTACHED FILES:

ADDITIONALS:
> The name Vantremo comes from "collectivity". With our name we want to pass the idea of the collectivity from the crowdsource work model.

> Our communication is directed to the Generation Y.

> Remember, we are a Startup! So we need a modern and simple site, something like the web 2.0 trends. It must be beautiful =)

> We arent a serious company. We are a young and fun company! Please, dont come with old fashionable company sites.

> Be creative =] !

Target Market(s)

Our target audience are young people around 20-35 years old. Generation Y (Millennial Generation)

Industry/Entity Type

Communication

Requirements
Must have
• We need a Web Design for our first site.

We need 5 pages:
- Home
- What is Crowdsourcing?
- Solutions
- About Us
- Blog

ABOUT THE COLORS TO USE: we would like some color to our background and titles. We like colors similars to our logo: really light blue ? light green/blue ? light grey ? light oranges ? I dont know, you guys knows more about that then me =)

Should not have
• Poor/serious/old fashionable designs

```html
<!DOCTYPE html>
<html lang="en">
<head>
<meta charset="utf-8">
<title>Vantremo</title>
<link href="https://fonts.googleapis.com/css2?family=Gelasio:wght@400;700&family=Arimo:wght@400&family=Nunito:wght@800&display=swap" rel="stylesheet">
<style>
  :root {
    --teal: #3aa6b5;
    --teal-dark: #2b8c9a;
    --ink: #1f1f1f;
    --body-text: #555555;
    --panel-dark: #2b2b2e;
    --nav-dark: #2e2e2e;
    --nav-mid: #444444;
    --frame: #9a9a9a;
    --box-bg: #f3f2f2;
    --white: #ffffff;
  }
  * { box-sizing: border-box; margin: 0; padding: 0; }
  html, body { width: 1159px; height: 1200px; overflow: hidden; background: var(--white); }
  body { position: relative; font-family: "Gelasio", Georgia, serif; color: var(--ink); }

  .brand { position: absolute; left: 48px; top: 40px; display: flex; align-items: center; gap: 14px; }
  .brand-dot { width: 72px; height: 72px; border-radius: 50%; background: var(--teal); }
  .brand-name { font-family: "Nunito", sans-serif; font-weight: 800; font-size: 78px; line-height: 1; color: var(--teal); letter-spacing: -1px; }

  .main-nav { position: absolute; left: 525px; top: 56px; width: 583px; height: 51px; display: flex; border-radius: 7px; overflow: hidden; background: linear-gradient(var(--nav-mid), var(--nav-dark)); }
  .main-nav a { display: flex; align-items: center; justify-content: center; color: var(--white); text-decoration: none; font-size: 16px; border-right: 1px solid #5a5a5a; }
  .main-nav a:last-child { border-right: none; }
  .main-nav .is-active { background: var(--teal); width: 222px; }
  .main-nav .nav-solutions { width: 139px; }
  .main-nav .nav-about { width: 129px; }
  .main-nav .nav-blog { width: 93px; }

  .hero { position: absolute; left: 42px; top: 156px; width: 1068px; height: 314px; border: 1px solid var(--frame); padding: 4px; display: flex; }
  .hero-photo { width: 787px; height: 304px; background: linear-gradient(100deg, #3a3a3c 0%, #8a8f96 40%, #dfe6ee 70%, #f3f6fa 100%); }
  .hero-panel { flex: 1; background: var(--panel-dark); padding: 22px 24px; position: relative; color: var(--white); }
  .hero-arrows { display: flex; gap: 8px; margin-bottom: 30px; }
  .hero-title { color: var(--teal); font-size: 22px; margin-bottom: 18px; }
  .hero-lead { font-size: 18px; line-height: 28px; }
  .hero-copy { font-size: 18px; line-height: 28px; color: #b8b8b8; }
  .btn-light { position: absolute; right: 20px; bottom: 25px; background: var(--white); color: var(--ink); font-weight: 700; font-size: 15px; padding: 2px 10px; border-radius: 3px; }

  .contact-tab { position: absolute; left: 1128px; top: 248px; width: 40px; height: 138px; background: linear-gradient(90deg, var(--teal), var(--teal-dark)); border-radius: 8px 0 0 8px; display: flex; align-items: center; justify-content: center; }
  .contact-tab span { transform: rotate(-90deg); color: var(--white); font-size: 15px; }

  .services { position: absolute; left: 40px; top: 509px; width: 1070px; height: 611px; background: var(--box-bg); border: 1px solid var(--frame); }
  .service { position: absolute; top: 30px; width: 316px; }
  .service-photo { width: 316px; height: 219px; box-shadow: 0 3px 6px rgba(0,0,0,.35); }
  .service h2 { font-weight: 400; font-size: 23px; text-align: center; margin-top: 23px; height: 66px; }
  .service p { font-size: 16px; line-height: 28px; color: var(--body-text); padding: 0 0 0 5px; width: 306px; }
  .service p strong { color: var(--ink); }
  .btn-dark { position: absolute; top: 486px; background: var(--ink); color: var(--white); font-size: 16px; width: 100px; height: 36px; border-radius: 4px; display: flex; align-items: center; justify-content: center; }
  .s1 { left: 28px; } .s1 .btn-dark { left: 218px; }
  .s2 { left: 375px; } .s2 .btn-dark { left: 218px; }
  .s3 { left: 721px; } .s3 .btn-dark { left: 218px; }
  .s1 .service-photo { background: linear-gradient(135deg, #e8eef4, #9fb4c8 55%, #2f3440); }
  .s2 .service-photo { background: linear-gradient(160deg, #6b7479, #3c4246 60%, #1e2224); }
  .s3 .service-photo { background: linear-gradient(180deg, #f0f0f0, #b9bcc0 60%, #5a5e63); }

  .site-footer { position: absolute; left: 40px; top: 1132px; width: 1070px; height: 67px; border: 1px solid var(--frame); display: flex; align-items: center; padding: 0 15px 0 38px; font-family: "Arimo", Arial, sans-serif; font-size: 16px; color: #333; }
  .footer-links { display: flex; gap: 17px; }
  .footer-links .sep { color: #555; }
  .follow { margin-left: auto; display: flex; align-items: center; gap: 10px; }
  .follow span { margin-right: 8px; }
  .social { width: 24px; height: 24px; border-radius: 3px; }
  .social-a { background: #3b5a9a; } .social-b { background: #3fa8d8; } .social-c { background: #d8d8d8; }
</style>
</head>
<body>
  <header>
    <div class="brand"><div class="brand-dot"></div><div class="brand-name">Vantremo</div></div>
    <nav class="main-nav">
      <a class="is-active" href="#">What is Crowdsourcing?</a>
      <a class="nav-solutions" href="#">Solutions</a>
      <a class="nav-about" href="#">About Us</a>
      <a class="nav-blog" href="#">Blog</a>
    </nav>
  </header>

  <section class="hero">
    <div class="hero-photo" role="img" aria-label="Business man and woman looking upward against a cloudy sky"></div>
    <div class="hero-panel">
      <div class="hero-arrows">
        <svg width="10" height="14" viewBox="0 0 10 14"><path d="M8 2 L3 7 L8 12" stroke="#aaa" stroke-width="2.5" fill="none"/></svg>
        <svg width="10" height="14" viewBox="0 0 10 14"><path d="M2 2 L7 7 L2 12" stroke="#aaa" stroke-width="2.5" fill="none"/></svg>
      </div>
      <h1 class="hero-title" style="font-weight:400">Vantremo Mission:-</h1>
      <p class="hero-lead">Here we tell our mission in a few lines.</p>
      <p class="hero-copy">Lorem ipsum dolor sit amet consectetur adipiscing elit.</p>
      <span class="btn-light">More</span>
    </div>
  </section>

  <div class="contact-tab"><span>Contact</span></div>

  <section class="services">
    <article class="service s1">
      <div class="service-photo" role="img" aria-label="Presenter addressing a meeting table"></div>
      <h2>CONSULTANCY</h2>
      <p><strong>Here we have a short description of our Consultancy service.</strong><br>Lorem ipsum dolor sit amet, consectetur adipiscing elit. Vestibulum lectus ante, lac-inia eu ultrices non, pellentesque at elit.</p>
      <span class="btn-dark">Read More</span>
    </article>
    <article class="service s2">
      <div class="service-photo" role="img" aria-label="Person touching a futuristic digital interface"></div>
      <h2>TECHONLOGY</h2>
      <p><strong>Here we have a short description of our technology service.</strong><br>Lorem ipsum dolor sit amet, consectetur adipiscing elit. Vestibulum lectus ante, lac-inia eu ultrices non, pellentesque at elit.</p>
      <span class="btn-dark">Read More</span>
    </article>
    <article class="service s3">
      <div class="service-photo" role="img" aria-label="Hand holding a network of people icons before a team"></div>
      <h2>Consultancy + Technology</h2>
      <p><strong>Here we have a short description of our Consultancy + Technology service.</strong><br>Lorem ipsum dolor sit amet, consectetur adipiscing elit. Vestibulum lectus ante, lac-inia eu ultrices non, pellentesque at elit.</p>
      <span class="btn-dark">Read More</span>
    </article>
  </section>

  <footer class="site-footer">
    <div class="footer-links">
      <span>Home</span><span class="sep">I</span>
      <span>What is Crowdsourcing?</span><span class="sep">I</span>
      <span>Solutions</span><span class="sep">I</span>
      <span>About us</span><span class="sep">I</span>
      <span>Blog</span>
    </div>
    <div class="follow">
      <span>Follow us :-</span>
      <div class="social social-a" role="img" aria-label="plimbook"></div>
      <div class="social social-b" role="img" aria-label="Social network"></div>
      <div class="social social-c" role="img" aria-label="Photo sharing network"></div>
    </div>
  </footer>
</body>
</html>
```